New Interrior Decoration company needs new website

We need a website for our new company specialising in interior decoration to residential and commercial markets.
We supply and install decorative and printed films for office and home decoration such as feature walls.
We would like to keep the design simple and clean.

Target Market(s)

Architects and interior designaers

Industry/Entity Type

It Company

Number of Pages Required

5+ page

Font styles to use
Sans Serif

Requirements
Must have
• Home page,
• Services/products page (split into commercial and residential)
• Gallery (split into commercial and residential)
• contact form and page
Nice to have
• Very clean and minimalistic design.

```html
<!DOCTYPE html>
<html lang="en">
<head>
<meta charset="utf-8">
<title>Larchmont Interiors</title>
<link href="https://fonts.googleapis.com/css2?family=Raleway:wght@400;500;700&family=Open+Sans:wght@400;600;700&family=Lato:wght@700;900&display=swap" rel="stylesheet">
<style>
:root{
  --blue:#0059b8;
  --dark:#393939;
  --darker:#333333;
  --text:#555555;
  --heading:#2b2b2b;
  --light:#ebebeb;
  --white:#ffffff;
  --rule:#d6d6d6;
}
*{box-sizing:border-box;margin:0;padding:0}
html,body{width:1200px;height:2449px;overflow:hidden}
body{position:relative;background:var(--white);font-family:"Open Sans",Arial,sans-serif;color:var(--text)}
.abs{position:absolute}

.hero{left:0;top:0;width:1200px;height:782px;
  background:linear-gradient(180deg,#4e514f 0%,#3f423f 45%,#5c5f5d 68%,#c9cccc 72%,#e4e6e6 100%)}
.hero-sofa{left:236px;top:400px;width:748px;height:260px;border-radius:60px 60px 30px 30px;
  background:linear-gradient(180deg,#d8dddf,#b9c0c2)}
.brand{left:0;top:150px;width:1200px;display:flex;justify-content:center;align-items:center;gap:22px}
.brand-mark{width:96px;height:96px;background:var(--blue)}
.brand-name{font-family:"Raleway",Arial,sans-serif;font-weight:700;font-size:66px;line-height:1;color:var(--white);letter-spacing:1px}
.tagline{left:0;top:312px;width:1200px;text-align:center;font-family:"Lato",Arial,sans-serif;font-weight:900;font-size:39px;color:var(--white)}

.nav{left:0;top:782px;width:1200px;height:62px;background:var(--blue)}
.nav ul{list-style:none;display:flex;position:absolute;left:77px;top:0;height:62px}
.nav li{height:62px;display:flex;align-items:center;padding:0 34px;font-family:"Raleway",Arial,sans-serif;font-size:21px;color:var(--white)}
.nav li.active{background:var(--dark)}

.section-title{left:0;width:1200px;text-align:center;font-family:"Raleway",Arial,sans-serif;font-weight:400;font-size:42px;color:var(--heading);line-height:1}
.section-title span{color:var(--blue)}
.welcome-text{left:170px;top:965px;width:860px;text-align:center;font-size:15.5px;line-height:24.5px;color:var(--text)}
.btn{display:flex;align-items:center;justify-content:center;background:var(--blue);color:var(--white);font-family:"Raleway",Arial,sans-serif;font-size:18px;border-radius:3px}

.call-band{left:77px;top:1167px;width:1046px;height:146px}
.call-text{left:100px;top:1214px;height:52px;display:flex;align-items:center;gap:14px;color:var(--white)}
.call-label{font-family:"Raleway",Arial,sans-serif;font-size:27px}
.call-icon{width:62px;height:62px;border:2px solid var(--white);border-radius:50%;display:flex;align-items:center;justify-content:center}
.call-number{font-family:"Open Sans",Arial,sans-serif;font-weight:700;font-size:31px}
.call-info{left:659px;top:1188px;width:440px;color:var(--white);font-size:16px;line-height:25px}
.call-mail{display:flex;align-items:center;gap:10px;margin-top:12px}

.service{width:400px;text-align:center}
.service-icon{width:124px;height:124px;border-radius:50%;background:var(--blue);margin:0 auto;display:flex;align-items:center;justify-content:center}
.service h3{font-family:"Raleway",Arial,sans-serif;font-weight:400;font-size:26px;color:var(--heading);margin-top:14px}
.service p{font-size:15.5px;line-height:24.5px;width:320px;margin:8px auto 0}
.read-more{font-family:"Raleway",Arial,sans-serif;font-size:18px;color:var(--blue);margin-top:4px;display:inline-flex;align-items:center;gap:6px}
.divider{left:600px;top:1449px;width:1px;height:271px;background:var(--rule)}

.gallery{left:0;top:1779px;width:1200px;height:438px;background:var(--light)}
.gallery-grid{left:77px;top:1905px;display:flex;gap:36px}
.gallery-item{width:234px;height:157px}

.footer{left:0;top:2217px;width:1200px;height:232px;background:var(--darker);color:var(--white)}
.footer-nav{left:79px;top:2252px;display:flex;gap:34px;font-family:"Open Sans",Arial,sans-serif;font-size:18px}
.socials{left:855px;top:2243px;display:flex;gap:26px}
.social{width:46px;height:46px;border:2px solid var(--white);border-radius:3px}
.social.filled{background:var(--white)}
.footer-rule{left:77px;top:2317px;width:1046px;height:1px;background:#555}
.footer-heading{left:79px;top:2337px;font-family:"Raleway",Arial,sans-serif;font-size:20px}
.footer-item{top:2372px;display:flex;align-items:center;gap:12px;font-size:15.5px;line-height:24px}
.footer-icon{width:41px;height:41px;background:var(--white);border-radius:3px;display:flex;align-items:center;justify-content:center;flex:none}
.copyright{left:889px;top:2365px;font-size:15.5px;line-height:25px}
</style>
</head>
<body>

<div class="abs hero" role="img" aria-label="Interior photo: white sofa with cushions against a grey textured wall"></div>
<div class="abs brand">
  <div class="brand-mark"></div>
  <div class="brand-name">LARCHMONT INTERIORS</div>
</div>
<div class="abs tagline">LOREM IPSUM IS DUMMY TEXT.</div>

<nav class="abs nav">
  <ul>
    <li class="active">HOME</li><li>ABOUT</li><li>SERVICES</li><li>GALLERY</li><li>CONTACT</li>
  </ul>
</nav>

<h1 class="abs section-title" style="top:899px">WELCOME TO <span>LARCHMONT INTERIORS</span></h1>
<p class="abs welcome-text">Lorem Ipsum is simply dummy text of the printing and typesetting industry. Lorem Ipsum has been the industry's standard dummy text ever since the 1500s, when an unknown printer took a galley of type and scrambled it to make a type specimen book.</p>
<div class="abs btn" style="left:517px;top:1059px;width:163px;height:51px">READ MORE</div>

<svg class="abs call-band" viewBox="0 0 1046 146" aria-hidden="true">
  <polygon points="0,0 553,0 508,146 0,146" fill="#0059b8"/>
  <polygon points="565,0 1046,0 1046,146 520,146" fill="#393939"/>
</svg>
<div class="abs call-text">
  <span class="call-label">CALL US NOW!</span>
  <span class="call-icon"><svg width="28" height="28" viewBox="0 0 24 24"><path fill="#fff" d="M6.6 10.8a15 15 0 0 0 6.6 6.6l2.2-2.2c.3-.3.7-.4 1-.2 1.1.4 2.3.6 3.6.6.6 0 1 .4 1 1V20c0 .6-.4 1-1 1C10.6 21 3 13.4 3 4c0-.6.4-1 1-1h3.5c.6 0 1 .4 1 1 0 1.3.2 2.5.6 3.6.1.3 0 .7-.2 1z"/></svg></span>
  <span class="call-number">123 456 7890</span>
</div>
<div class="abs call-info">
  <p>Lorem Ipsum is simply dummy text of the printing and typesetting industry lorem Ipsum has been.</p>
  <p class="call-mail"><svg width="18" height="14" viewBox="0 0 18 14"><rect x="1" y="1" width="16" height="12" fill="none" stroke="#fff" stroke-width="1.6"/><path d="M1 1l8 7 8-7" fill="none" stroke="#fff" stroke-width="1.6"/></svg>info@larchmontinteriors.com</p>
</div>

<h2 class="abs section-title" style="top:1372px">SERVICES <span>WE PROVIDE</span></h2>
<div class="abs divider"></div>
<div class="abs service" style="left:181px;top:1439px">
  <div class="service-icon"><svg width="62" height="54" viewBox="0 0 62 54"><path fill="#fff" d="M31 2 2 28h8v24h16V36h10v16h16V28h8L46 15V5h-7v4z"/></svg></div>
  <h3>Residential Interiors</h3>
  <p>Lorem Ipsum is simply dummy text of the printing and typesetting industry. Lorem Ipsum has been the industry.</p>
  <span class="read-more">READ MORE <svg width="14" height="14" viewBox="0 0 14 14"><path d="M2 2l5 5-5 5M7 2l5 5-5 5" fill="none" stroke="#0059b8" stroke-width="2"/></svg></span>
</div>
<div class="abs service" style="left:623px;top:1439px">
  <div class="service-icon"><svg width="64" height="56" viewBox="0 0 64 56"><g fill="#fff"><rect x="4" y="18" width="18" height="36"/><rect x="24" y="4" width="22" height="50"/><rect x="48" y="24" width="12" height="30"/></g><g fill="#0059b8"><rect x="28" y="10" width="4" height="4"/><rect x="37" y="10" width="4" height="4"/><rect x="28" y="20" width="4" height="4"/><rect x="37" y="20" width="4" height="4"/><rect x="28" y="30" width="4" height="4"/><rect x="37" y="30" width="4" height="4"/><rect x="9" y="26" width="4" height="4"/><rect x="9" y="36" width="4" height="4"/></g></svg></div>
  <h3>Commercial Interiors</h3>
  <p>Lorem Ipsum is simply dummy text of the printing and typesetting industry. Lorem Ipsum has been the industry.</p>
  <span class="read-more">READ MORE <svg width="14" height="14" viewBox="0 0 14 14"><path d="M2 2l5 5-5 5M7 2l5 5-5 5" fill="none" stroke="#0059b8" stroke-width="2"/></svg></span>
</div>

<section class="abs gallery"></section>
<h2 class="abs section-title" style="top:1841px">LATEST <span>GALLERY</span></h2>
<div class="abs gallery-grid">
  <div class="gallery-item" role="img" aria-label="Dark lounge interior with black vases" style="background:linear-gradient(135deg,#6b5a48,#2a2420)"></div>
  <div class="gallery-item" role="img" aria-label="Living room with white lounge chair and red wall" style="background:linear-gradient(135deg,#5a2a1a,#9a5a3a 60%,#3a2a2a)"></div>
  <div class="gallery-item" role="img" aria-label="Hallway with stone textured feature wall" style="background:linear-gradient(135deg,#a9aca6,#6d726c)"></div>
  <div class="gallery-item" role="img" aria-label="Room with red brick feature wall and black sofa" style="background:linear-gradient(135deg,#8e3a2a,#b9a78a 70%,#d8d6cc)"></div>
</div>
<div class="abs btn" style="left:525px;top:2098px;width:150px;height:49px">VIEW ALL</div>

<footer class="abs footer"></footer>
<div class="abs footer-nav" style="color:#fff"><span>Home</span><span>About</span><span>Services</span><span>Gallery</span><span>Contact</span></div>
<div class="abs socials" aria-label="Social links">
  <span class="social filled"></span><span class="social"></span><span class="social"></span><span class="social"></span>
</div>
<div class="abs footer-rule"></div>
<div class="abs footer-heading" style="color:#fff">Contact Us</div>
<div class="abs footer-item" style="left:77px;color:#fff">
  <span class="footer-icon"><svg width="16" height="22" viewBox="0 0 16 22"><path fill="#333" d="M8 0a8 8 0 0 0-8 8c0 6 8 14 8 14s8-8 8-14a8 8 0 0 0-8-8zm0 11a3 3 0 1 1 0-6 3 3 0 0 1 0 6z"/></svg></span>
  <span style="width:160px">Lorem Ipsum is dummy text of the printing.</span>
</div>
<div class="abs footer-item" style="left:348px;color:#fff;font-weight:600">
  <span class="footer-icon"><svg width="20" height="20" viewBox="0 0 24 24"><path fill="#333" d="M6.6 10.8a15 15 0 0 0 6.6 6.6l2.2-2.2c.3-.3.7-.4 1-.2 1.1.4 2.3.6 3.6.6.6 0 1 .4 1 1V20c0 .6-.4 1-1 1C10.6 21 3 13.4 3 4c0-.6.4-1 1-1h3.5c.6 0 1 .4 1 1 0 1.3.2 2.5.6 3.6.1.3 0 .7-.2 1z"/></svg></span>
  <span>123 456 7890</span>
</div>
<div class="abs footer-item" style="left:602px;color:#fff">
  <span class="footer-icon"><svg width="20" height="15" viewBox="0 0 18 14"><rect x="1" y="1" width="16" height="12" fill="none" stroke="#333" stroke-width="1.6"/><path d="M1 1l8 7 8-7" fill="none" stroke="#333" stroke-width="1.6"/></svg></span>
  <span>info@larchmontinteriors.com</span>
</div>
<div class="abs copyright" style="color:#fff"><strong>© LARCHMONT INTERIORS</strong> - 2016.<br>All Rights Reserved.</div>

</body>
</html>
```